Flyer for our prophetic church event

I need a flyer designed for the launching of our "7 Radiant Harvest Gatherings" event. This event should high light the next 7 Sundays starting on February the 11th, 2018

Event Name:
7 Radiant Harvests

Event Slogan or topic:
Go and tell John ... the blind see, the lame walk, the lepers are cleansed, the deaf hear, the dead are raised,
the poor have the gospel preached to them.

Speaker:
Prophet Marcus Obuya

February 11th
February 18th
February 25th
March 4th
March 11th
March 18th
March 25th

Location:
Talvor Community Center
382 Wendle Street
Portland, ME 04981
United States

Time:
10:00AM - 12:00PM

We welcome you all in the name of Jesus Christ

Contact Info:
Tel:+1(555) 302 1189 - Email:contact@mirovalefold.org - Website: http://velosa.org

Target Market(s)

Young adults

Industry/Entity Type

Church

Font styles to use
Other font styles liked:
• Surprise me, I trust the designers skills

Colors

Designer to choose colors to be used in the design.

Requirements
Must have
• The Velosa logo
• Marcus Obuya's picture
• The
Should not have
• The background of the Marcus Obuya's picture

```html
<!DOCTYPE html>
<html lang="en">
<head>
<meta charset="utf-8">
<title>7 Radiant Harvests</title>
<link rel="stylesheet" href="https://fonts.googleapis.com/css2?family=Cinzel:wght@700;900&family=Alegreya+SC:wght@500&family=Pinyon+Script&family=Playfair+Display:ital,wght@1,700&family=Montserrat:wght@500;600;700;800&family=Alfa+Slab+One&display=swap">
<style>
:root{
  --page:#ffffff;
  --night:#1a1526;
  --violet:#4a3560;
  --plum:#6b4a78;
  --beam:#f3c98a;
  --crimson:#8e1418;
  --gold:#f2e33a;
  --sky:#2aa6e0;
  --ink:#161616;
  --navy:#1c3b5e;
  --white:#ffffff;
  --black:#000000;
}
*{margin:0;padding:0;box-sizing:border-box}
html,body{width:939px;height:1200px;overflow:hidden;background:var(--page)}
.flyer{position:relative;width:939px;height:1200px;background:var(--page)}
.stage{
  position:absolute;left:25px;top:25px;width:888px;height:1059px;overflow:hidden;
  background:
    radial-gradient(ellipse 300px 620px at 240px 560px, rgba(243,201,138,.55), rgba(243,201,138,0) 70%),
    radial-gradient(ellipse 520px 420px at 60px 160px, rgba(230,120,60,.55), rgba(230,120,60,0) 70%),
    radial-gradient(ellipse 700px 600px at 330px 620px, var(--plum), rgba(107,74,120,0) 75%),
    linear-gradient(180deg, var(--night) 0%, var(--violet) 55%, #2b2236 100%);
}
.title{
  position:absolute;left:-100px;right:-100px;top:72px;text-align:center;white-space:nowrap;
  font-family:"Cinzel",serif;font-weight:900;font-size:76px;line-height:1;
  color:var(--crimson);letter-spacing:-1px;
  text-shadow:0 0 6px #fff,0 0 14px rgba(255,255,255,.8);
  transform:scaleX(.8);transform-origin:center;
}
.title-seven{font-size:92px}
.verse{
  position:absolute;left:0;right:0;top:186px;text-align:center;white-space:nowrap;
  font-family:"Alegreya SC",serif;font-weight:500;font-size:26px;line-height:31px;
  color:var(--gold);text-shadow:0 1px 3px rgba(0,0,0,.6);
}
.speaker-label{
  position:absolute;left:82px;top:340px;font-family:"Pinyon Script",cursive;
  font-size:46px;color:var(--ink);
}
.prophet{
  position:absolute;left:180px;width:200px;top:398px;text-align:center;
  font-family:"Playfair Display",serif;font-style:italic;font-weight:700;
  font-size:32px;color:var(--white);text-shadow:0 1px 3px rgba(0,0,0,.5);
}
.name{
  position:absolute;left:20px;width:500px;top:438px;text-align:center;white-space:nowrap;
  font-family:"Montserrat",sans-serif;font-weight:800;font-size:40px;
  color:var(--sky);letter-spacing:.5px;text-shadow:0 0 6px rgba(255,255,255,.6);
}
.dates{
  position:absolute;left:158px;top:500px;list-style:none;
  font-family:"Montserrat",sans-serif;font-weight:700;font-size:20px;line-height:28px;color:var(--ink);
}
.venue,.time{
  position:absolute;left:30px;width:480px;text-align:center;white-space:nowrap;
  font-family:"Montserrat",sans-serif;font-weight:700;color:var(--ink);
}
.venue{top:712px;font-size:19px;line-height:28px}
.time{top:796px;font-size:20px;line-height:32px}
.label{font-size:19px}
.portrait{
  position:absolute;left:485px;top:323px;width:403px;height:736px;
  background:radial-gradient(ellipse 180px 260px at 210px 200px, rgba(120,80,60,.55), rgba(120,80,60,0) 75%),
             linear-gradient(180deg, rgba(40,30,40,0) 0%, rgba(20,20,28,.85) 40%, #141418 100%);
  border-radius:180px 180px 0 0;
}
.brand{
  position:absolute;left:27px;top:883px;width:236px;height:163px;background:var(--navy);
  display:flex;align-items:center;justify-content:center;gap:12px;
}
.brand-dot{width:18px;height:18px;border-radius:50%;background:var(--white)}
.brand-name{font-family:"Cinzel",serif;font-weight:700;font-size:44px;color:var(--white);letter-spacing:1px}
.welcome{
  position:absolute;left:290px;width:560px;top:945px;text-align:center;white-space:nowrap;
  font-family:"Alfa Slab One",serif;font-size:30px;line-height:42px;color:var(--black);
  -webkit-text-stroke:1px var(--white);
  text-shadow:0 0 2px var(--white),0 0 4px var(--white);
}
.contact{
  position:absolute;left:25px;top:1084px;width:888px;height:89px;background:var(--black);
  color:var(--white);text-align:center;font-family:"Montserrat",sans-serif;font-weight:600;
  font-size:17px;line-height:26px;padding-top:16px;white-space:nowrap;
}
</style>
</head>
<body>
<div class="flyer">
  <section class="stage">
    <h1 class="title"><span class="title-seven">7</span> RADIANT HARVESTS</h1>
    <p class="verse">Go and tell John … the blind see, the<br>lame walk, the lepers are cleansed, the deaf hear,<br>the dead are raised, the poor have the gospel<br>preached to them.</p>
    <div class="speaker-label">Speaker:</div>
    <div class="prophet">Prophet</div>
    <div class="name">MARCUS OBUYA</div>
    <ul class="dates">
      <li>February 11th</li>
      <li>February 18th</li>
      <li>February 25th</li>
      <li>March 4th</li>
      <li>March 11th</li>
      <li>March 18th</li>
      <li>March 25th</li>
    </ul>
    <div class="venue"><span class="label">Location:</span><br>Talvor Community Center 382<br>Wendle Street Portland, ME 04981</div>
    <div class="time"><span class="label">Time:</span><br>10:00AM - 12:00PM</div>
    <div class="portrait" role="img" aria-label="Photo of the speaker, Prophet Marcus Obuya, in a dark suit and blue shirt"></div>
    <div class="brand"><span class="brand-dot"></span><span class="brand-name">VELOSA</span></div>
    <p class="welcome">We welcome you all in the<br>name of Jesus Christ</p>
  </section>
  <footer class="contact">Contact Info:<br>Tel:+1(555) 302 1189 - Email:contact@mirovalefold.org - Website: http://velosa.org</footer>
</div>
</body>
</html>
```